Need Power Point Presentation - That incorporates New Logo

We have a new logo and would like to incorporate it into a Power Point template. We are looking for title page, 2 body pages and a closing page design. If you have any questions please let me know. New logo is attached.

```html
<!DOCTYPE html>
<html lang="en">
<head>
<meta charset="utf-8">
<title>Who We Are</title>
<link rel="stylesheet" href="https://fonts.googleapis.com/css2?family=Open+Sans:wght@300;400&display=swap">
<style>
  :root {
    --page-bg: #ffffff;
    --footer-bg: #eeeeee;
    --heading-pink: #e2137c;
    --body-grey: #8b8b8b;
    --title-grey: #4a4a4a;
    --link-blue: #1f7bb8;
    --frame-blue: #4a9fd0;
    --accent-soft: #e3f3fa;
    --accent-softer: #f6fbfd;
    --brand-blue: #3b8ec8;
  }
  * { margin: 0; padding: 0; box-sizing: border-box; }
  html, body { width: 1200px; height: 658px; overflow: hidden; background: var(--page-bg); }
  body { font-family: "Open Sans", "Segoe UI", sans-serif; font-weight: 300; position: relative; }

  .slide { position: relative; width: 1200px; height: 658px; overflow: hidden; }

  .photo-grid .tile { position: absolute; width: 78px; height: 71px; }
  .tile--framed { border: 1px solid var(--frame-blue); }

  .title-accent {
    position: absolute; left: 720px; top: 0; width: 350px; height: 157px;
    background: radial-gradient(ellipse at 45% 45%, var(--accent-soft), var(--accent-softer) 70%, var(--page-bg));
  }
  .section-title {
    position: absolute; left: 790px; top: 38px; width: 170px;
    text-align: center; font-size: 35px; line-height: 31px; font-weight: 300;
    letter-spacing: -1.5px; color: var(--title-grey);
  }

  .content { position: absolute; left: 342px; top: 171px; width: 780px; }
  .content__heading { font-size: 16.5px; font-weight: 400; color: var(--heading-pink); letter-spacing: -0.4px; margin-bottom: 25px; }
  .content__text { font-size: 16px; line-height: 25px; color: var(--body-grey); letter-spacing: -0.35px; margin-bottom: 24px; white-space: nowrap; }
  .content__link { color: var(--link-blue); }

  .footer { position: absolute; left: 0; top: 601px; width: 1200px; height: 57px; background: var(--footer-bg); }
  .brand { position: absolute; right: 108px; top: 18px; display: flex; align-items: center; gap: 6px; }
  .brand__dot { width: 10px; height: 10px; border-radius: 50%; background: var(--brand-blue); }
  .brand__name { font-size: 17px; font-weight: 400; color: var(--brand-blue); letter-spacing: 0.5px; }
</style>
</head>
<body>
<main class="slide">
  <div class="photo-grid">
    <div class="tile tile--framed" style="left:-12px;top:-4px;height:71px;background:linear-gradient(135deg,#e8e2cf,#3a6fb0);" role="img" aria-label="Photo of a branded insulated bag"></div>
    <div class="tile" style="left:66px;top:0;height:66px;background:linear-gradient(135deg,#0f3b3c,#7fb0a8);" role="img" aria-label="Photo of a diver underwater"></div>
    <div class="tile" style="left:145px;top:0;height:66px;background:linear-gradient(135deg,#1d4f8a,#1b2a24);" role="img" aria-label="Photo of a locomotive"></div>
    <div class="tile" style="left:224px;top:0;height:66px;background:linear-gradient(135deg,#dcdcd8,#5c5a3c);" role="img" aria-label="Photo of a soldier in snow"></div>
    <div class="tile" style="left:303px;top:0;height:66px;background:linear-gradient(180deg,#8fb6dc,#a8a297);" role="img" aria-label="Photo of an industrial plant"></div>
    <div class="tile" style="left:66px;top:67px;background:linear-gradient(135deg,#8fb2c9,#704c33);" role="img" aria-label="Photo of a loading facility"></div>
    <div class="tile" style="left:145px;top:67px;background:linear-gradient(135deg,#5f6466,#2e3234);" role="img" aria-label="Photo of textured material close-up"></div>
    <div class="tile" style="left:224px;top:67px;background:linear-gradient(135deg,#2f7fd0,#a9d2f2);" role="img" aria-label="Photo of blue aircraft seats"></div>
    <div class="tile tile--framed" style="left:145px;top:139px;background:linear-gradient(135deg,#f4f4f4 15%,#c49a62 45%,#6d86b7 85%);" role="img" aria-label="Photo of quilted insulation panels"></div>
  </div>

  <div class="title-accent" role="img" aria-label="Decorative light blue brand ornament behind the section title"></div>
  <h1 class="section-title">WHO WE<br>ARE</h1>

  <section class="content">
    <h2 class="content__heading">Lorem ipsum dolor sit amet</h2>
    <p class="content__text">consectetuer adipiscing elit, sed diam nonummy nibh euismod tincidunt ut laoreet dolore magna aliquam erat<br>volutpat. Ut wisi enim ad minim veniam, quis nostrud exerci tation ullamcorper suscipit lobortis nisl ut aliquip ex<br>ea commodo consequat.&nbsp;&nbsp; Duis autem vel eum iriure dolor in hendrerit in vulputate velit esse molestie conse-<br>quat, vel illum dolore eu feugiat n<span class="content__link">ulla facilisis at vero</span> eros et accumsan et iusto odio dignissim qui blandit<br>praesent luptatum zzril delenit augue duis dolore te feugait nulla facilisi.</p>
    <p class="content__text">Duis autem vel eum iriure dolor in hendrerit in vulputate velit esse molestie consequat, vel illum dolore eu<br>feugiat nulla facilisis at vero eros et accumsan et iusto odio dignissim qui blandit praesent luptatum zzril delenit<br>augue duis dolore te feugait nulla facilisi.</p>
  </section>

  <footer class="footer">
    <div class="brand">
      <span class="brand__dot"></span>
      <span class="brand__name">NORTHWEAVE</span>
    </div>
  </footer>
</main>
</body>
</html>
```